Request for Business Card Design

Hi. My name is Marlena, I am looking for a new business card design for my company, Quillbrook Sensing Systems, LLC. I really like the design you did for Tavel Harvest and was hoping you could do something similar using our full logo and our mark. I am also open to any raised texture design using our mark. I have attached our full logo, which would need to be somewhere on the card, as well as the mark in both outline and full form, as well as our brand colors / guide. The card does not have to be white, as long as our logo and mark appear. I actually like darker colored business cards more, but am open to all options. If you are interested in working with me, please let me know. We would also take the business card design into letterhead design if you can do that.

```html
<!DOCTYPE html>
<html lang="en">
<head>
<meta charset="utf-8">
<title>Quillbrook Sensing Systems – Business Card</title>
<link rel="stylesheet" href="https://fonts.googleapis.com/css2?family=Barlow:wght@300;400;600;700&display=swap">
<style>
  :root {
    --backdrop: #7f97ba;
    --brand-green: #7cc243;
    --brand-green-light: #93d05c;
    --charcoal: #4a4a4a;
    --charcoal-light: #5e5e5e;
    --paper: #ffffff;
    --ink: #3a3a3a;
    --muted: #d6d6d6;
  }
  * { margin: 0; padding: 0; box-sizing: border-box; }
  html, body {
    width: 1200px; height: 876px; overflow: hidden;
    background: var(--backdrop);
    font-family: "Barlow", Arial, sans-serif;
  }
  .canvas {
    width: 1200px; height: 876px;
    display: flex; align-items: center; justify-content: center; gap: 40px;
  }
  .card {
    width: 540px; height: 309px;
    position: relative; overflow: hidden;
    box-shadow: 0 10px 24px rgba(30, 45, 80, 0.35);
  }

  /* Back: contact side */
  .card-back { display: flex; background: var(--paper); }
  .contact-panel {
    width: 46%; height: 100%;
    background: linear-gradient(150deg, var(--charcoal-light), var(--charcoal));
    padding: 34px 26px 0 20px;
    text-align: right; color: var(--muted);
  }
  .person-name {
    font-size: 25px; letter-spacing: 0.5px; line-height: 1;
    text-transform: uppercase;
  }
  .person-name .given { color: var(--brand-green); font-weight: 600; }
  .person-name .family { color: var(--paper); font-weight: 300; }
  .person-role { font-size: 14px; font-weight: 300; margin-top: 4px; color: var(--muted); }
  .contact-list { list-style: none; margin-top: 34px; }
  .contact-list li {
    display: flex; justify-content: flex-end; align-items: center; gap: 8px;
    font-size: 14px; font-weight: 300; line-height: 1.25; margin-bottom: 7px;
  }
  .contact-list .address { align-items: flex-start; }
  .contact-icon { width: 16px; height: 16px; flex: none; }
  .logo-panel {
    flex: 1; display: flex; align-items: center; justify-content: center;
  }

  /* Brand lockup */
  .brand-lockup { display: flex; align-items: center; gap: 12px; }
  .brand-dot { width: 40px; height: 40px; border-radius: 50%; flex: none; }
  .brand-text { font-weight: 700; text-transform: uppercase; line-height: 1; }
  .brand-text .brand-name { display: block; font-size: 34px; letter-spacing: 2px; }
  .brand-text .brand-tag { display: block; font-size: 13px; letter-spacing: 1.2px; margin-top: 4px; }
  .logo-panel .brand-dot { background: #2e9fc8; }
  .logo-panel .brand-text { color: var(--ink); }

  /* Front: brand side */
  .card-front {
    background: linear-gradient(160deg, var(--brand-green-light), var(--brand-green));
    display: flex; align-items: center; justify-content: center;
  }
  .card-front .brand-dot { width: 52px; height: 52px; background: var(--paper); }
  .card-front .brand-text { color: var(--paper); }
  .card-front .brand-name { font-size: 44px; }
  .card-front .brand-tag { font-size: 15px; }
</style>
</head>
<body>
<main class="canvas">
  <section class="card card-back" aria-label="Business card, contact side">
    <div class="contact-panel">
      <p class="person-name"><span class="given">Marlena</span><span class="family">Hale</span></p>
      <p class="person-role">Director</p>
      <ul class="contact-list">
        <li>+000 12345 6789
          <svg class="contact-icon" viewBox="0 0 16 16" aria-hidden="true"><circle cx="8" cy="8" r="8" fill="var(--brand-green)"/><rect x="5.5" y="3.5" width="5" height="9" rx="1" fill="none" stroke="#fff" stroke-width="1.2"/><circle cx="8" cy="11" r="0.6" fill="#fff"/></svg>
        </li>
        <li>urname@email.com
          <svg class="contact-icon" viewBox="0 0 16 16" aria-hidden="true"><circle cx="8" cy="8" r="8" fill="var(--brand-green)"/><rect x="4" y="5" width="8" height="6" fill="none" stroke="#fff" stroke-width="1.1"/><path d="M4 5l4 3.5L12 5" fill="none" stroke="#fff" stroke-width="1.1"/></svg>
        </li>
        <li class="address">Street Address Here<br>Larkport, 2222
          <svg class="contact-icon" viewBox="0 0 16 16" aria-hidden="true"><circle cx="8" cy="8" r="8" fill="var(--brand-green)"/><path d="M8 13s-3.2-3.6-3.2-6a3.2 3.2 0 0 1 6.4 0c0 2.4-3.2 6-3.2 6z" fill="#fff"/><circle cx="8" cy="7" r="1.2" fill="var(--brand-green)"/></svg>
        </li>
      </ul>
    </div>
    <div class="logo-panel">
      <div class="brand-lockup">
        <span class="brand-dot" aria-hidden="true"></span>
        <p class="brand-text"><span class="brand-name">Quillbrook</span><span class="brand-tag">Sensing Systems</span></p>
      </div>
    </div>
  </section>

  <section class="card card-front" aria-label="Business card, brand side">
    <div class="brand-lockup">
      <span class="brand-dot" aria-hidden="true"></span>
      <p class="brand-text"><span class="brand-name">Quillbrook</span><span class="brand-tag">Sensing Systems</span></p>
    </div>
  </section>
</main>
</body>
</html>
```